Mend ORX Syndrome (Non-Profit) Tri-Fold Brochure Design

We have put together the content for a brochure that we will distribute to doctors, researchers and patients about our non-profit. We would like the design of the brochure to look more professional and have nice aesthetics. It needs to incorporate all of the content in the attached Word file. We will have printed once we have a finished design.

Target Market(s)

Medical

Industry/Entity Type

Non Profit

Font styles to use
Serif
Sans Serif

Colors
33a6d7

Requirements
Must have
• Must include all content provided. Professional.
Nice to have
• Colors

```html
<!DOCTYPE html>
<html lang="en">
<head>
<meta charset="utf-8">
<title>Mend ORX Syndrome – Tri-Fold Brochure</title>
<link href="https://fonts.googleapis.com/css2?family=Montserrat:wght@600;700&family=PT+Sans:wght@400;700&display=swap" rel="stylesheet">
<style>
:root{
  --brand:#2ba3cf;
  --deep:#1a7ea8;
  --panel:#1689b3;
  --panel-dark:#136f96;
  --ink:#1d1d1d;
  --paper:#ffffff;
  --fog:#e3e4e6;
  --bg:#f2f2f2;
  --yellow:#f5b90c;
  --yellow-side:#b88a06;
  --orange:#e1762a;
  --orange-side:#a8561c;
  --grey:#8e8f93;
  --grey-side:#5f6064;
  --blue:#2f66c7;
  --green:#5aa53b;
  --olive:#a0a64a;
}
*{box-sizing:border-box;margin:0;padding:0}
html,body{width:1200px;height:1200px;overflow:hidden;background:var(--bg)}
body{font-family:"PT Sans",sans-serif;color:var(--ink)}
.stage{position:absolute;left:243px;top:16px;width:794px;height:1290px;transform:scale(0.905);transform-origin:0 0}
.spread{position:absolute;left:0;width:794px;height:617px;display:flex;background:var(--paper);box-shadow:0 6px 14px rgba(0,0,0,.15)}
.spread--outside{top:0}
.spread--inside{top:673px}
.panel{position:relative;height:100%;overflow:hidden}
p{font-size:10.6px;line-height:1.36}
.just{text-align:justify}
.tab{display:inline-block;background:var(--panel);color:#fff;font-family:"Montserrat",sans-serif;font-weight:700;font-size:13.5px;padding:3px 10px 3px 17px;letter-spacing:.2px}
.sub{color:var(--brand);font-weight:700;font-size:11.5px;margin-top:6px}
ul.bullets{list-style:none;font-size:10.6px;line-height:1.9}
ul.bullets li::before{content:"• "}

/* outside left */
.p-about{width:260px;background:linear-gradient(90deg,#fff 55%,var(--fog))}
.p-about .tab{margin-top:28px}
.p-about .copy{padding:0 11px 0 17px}
.p-about .copy p{margin-top:14px}
.p-about .copy p:first-child{margin-top:18px}
.pie{position:absolute;left:10px;top:436px}

/* outside middle */
.p-support{width:263px;background:linear-gradient(90deg,var(--fog),#fff 40%,#fff 60%,var(--fog));text-align:center}
.headline{margin-top:12px;color:var(--deep);font-family:"Montserrat",sans-serif;font-weight:600;font-size:22px;line-height:1.1}
.headline span{display:block;color:var(--ink);font-size:16px}
.rule{width:190px;height:1px;background:var(--deep);margin:5px auto 0}
.support-box{position:relative;margin:26px 14px 0;border:1.5px solid var(--deep);border-top:none;padding:16px 4px 8px;text-align:justify}
.support-box .tab{position:absolute;top:-11px;left:21px;padding:3px 16px;font-size:14px;text-align:center}
.support-box p{font-size:10.2px;line-height:1.4}
.offer{margin-top:20px;font-weight:700;font-size:10.6px;line-height:1.35}
.links{margin:14px 0 0 60px;text-align:left;list-style:none;font-size:10.6px;line-height:1.9}
.links li::before{content:"• ";color:var(--deep)}
.contact{margin-top:14px;font-size:10.6px;line-height:1.35}
.contact svg{display:block;margin:0 auto 2px}
.contact + .contact{margin-top:16px}
.badge{margin:18px auto 0;width:170px;height:78px;border:1px solid var(--deep);background:linear-gradient(#eef5f8,#dbe9ef)}

/* outside right */
.p-cover{width:271px;background:var(--paper)}
.brand{height:97px;display:flex;align-items:center;justify-content:center;gap:8px}
.brand i{width:14px;height:14px;border-radius:50%;background:var(--brand)}
.brand b{font-family:"Montserrat",sans-serif;font-weight:700;color:var(--brand);font-size:18px}
.ask{background:var(--brand);padding:5px 6px 6px}
.ask-in{background:var(--panel-dark);padding:10px 8px 12px 10px;color:#fff}
.ask h2{font-family:"Montserrat",sans-serif;font-size:13.5px;line-height:1.25;background:var(--panel);margin:-10px -8px 8px -10px;padding:8px 10px 6px}
.ask ul{list-style:none;font-family:"Montserrat",sans-serif;font-weight:700;font-size:15px;line-height:1.6}
.ask li svg{vertical-align:-1px;margin-right:5px}
.lab-photo{height:148px;background:linear-gradient(110deg,#f3f4f6 0%,#d8dde3 45%,#9aa3ae 100%)}
.cover-band{background:var(--panel-dark);color:#fff;text-align:center;padding:6px 10px;font-size:10.4px;line-height:1.3}
.cover-name{background:var(--brand);color:#fff;text-align:center;font-family:"Montserrat",sans-serif;font-weight:700;font-size:28px;letter-spacing:1px;padding:3px 0 0}
.cover-foot{background:var(--panel-dark);color:#fff;text-align:center;padding:5px 8px 8px;font-size:9.6px;line-height:1.3;height:86px}
.pill{display:inline-block;margin-top:7px;background:#fff;color:var(--deep);border-radius:12px;padding:3px 18px;font-family:"Montserrat",sans-serif;font-weight:700;font-size:11.5px;letter-spacing:1.2px}

/* inside */
.p-symptoms{width:258px;padding-right:8px}
.p-symptoms .tab,.p-diag .tab{margin-top:10px;padding-left:11px;padding-right:24px}
.p-symptoms .copy{padding:3px 0 0 11px}
.p-research{width:266px;background:var(--fog)}
.dna-photo{height:162px;background:linear-gradient(160deg,#0c2c55,#2a6db1 55%,#d9e6f2)}
.rally{text-align:center;background:linear-gradient(#d9e6f2,var(--fog));padding:0 0 4px;margin-top:-10px}
.rally b{display:block;font-size:14.5px;line-height:1.3}
.rally strong{display:block;color:var(--brand);font-family:"Montserrat",sans-serif;font-size:22px;margin-top:4px}
.p-research .tab{padding-left:12px;padding-right:8px}
.p-research .copy{padding:3px 11px 0 11px}
.enroll{margin:8px 2px 0;background:var(--brand);padding:4px}
.enroll div{background:var(--panel-dark);color:#fff;text-align:center;font-family:"Montserrat",sans-serif;font-weight:700;font-size:12.5px;line-height:1.35;padding:6px 8px}
.site{text-align:center;margin-top:6px;font-size:11.5px;line-height:1.35}
.site b{display:block;color:var(--brand);font-size:18px;font-weight:700}
.p-research .copy.low p{margin-top:8px}
.registry{position:absolute;left:0;bottom:0;width:100%;height:36px;background:linear-gradient(90deg,#fff 35%,#c8d8e4)}
.registry b{position:absolute;left:8px;top:4px;color:var(--deep);font-size:11px}
.registry small{position:absolute;left:8px;top:18px;font-size:6.5px;color:var(--deep);width:90px;line-height:1.1}
.p-diag{width:270px}
.p-diag .copy{padding:3px 11px 0 11px}
.p-diag .copy p + p{margin-top:8px}
.doc{margin-top:6px;font-size:9.8px;line-height:1.3}
.doc b{display:block;color:var(--deep);font-size:13.5px;font-weight:400}
.doc svg{vertical-align:-1px;margin-right:4px}
.protein{margin-top:12px;height:222px;background:radial-gradient(ellipse at 45% 55%,#1d54b8,#0a1a3a 55%,#000 85%)}
.p-diag .treat{margin-top:6px}
</style>
</head>
<body>
<main class="stage">

  <section class="spread spread--outside">
    <article class="panel p-about">
      <h2 class="tab">What is IBMPFD?</h2>
      <div class="copy">
        <p class="just">Inclusion Body Myopathy associated with Paget's disease of bone and Frontotemporal Dementia is an autosomal dominant mutation in chromosome 9 of the VCP (Valosin Containing Protein) gene. Given the interaction with other genetic diseases, this mutation may also be known as VCP Disease or Disorder.</p>
        <p class="just">Some patients have familial Amyotrophic Lateral Sclerosis (ALS or Lou Gehrig's disease) or Parkinson's which has been shown to have a pathogenic variant in VCP.</p>
      </div>
      <h2 class="tab" style="margin-top:20px">Penetrance by Phenotype</h2>
      <div class="copy">
        <p style="margin-top:14px">The frequency that IBMPFD or VCP Disease manifests itself in one, two,or threeprimary disorders.</p>
        <ul class="bullets" style="margin:10px 0 0 14px">
          <li>IBM: Inclusion Body Myopathy</li>
          <li>PDB:&nbsp; Paget's Disease of the Bone</li>
          <li>FTD: Frontotemporal Dementia</li>
        </ul>
      </div>
      <svg class="pie" width="245" height="150" viewBox="0 0 245 150" role="img" aria-label="3D pie chart of IBMPFD phenotype frequencies">
        <g font-family="PT Sans, sans-serif" font-size="5.5" fill="#333">
          <text x="44" y="10">PDB only - 5%</text>
          <text x="86" y="7">FTD only - 3%</text>
          <text x="139" y="10">IBM, PDB, and FTD - 10%</text>
          <text x="20" y="20">PDB &amp; FTD - 1%</text>
          <text x="191" y="25">IBM &amp; FTD - 16%</text>
          <text x="4" y="33">IBM &amp; PDB - 27%</text>
          <text x="185" y="145">IBM only - 37%</text>
        </g>
        <g transform="translate(0 6)">
          <!-- side walls -->
          <path d="M223 68 A100 46 0 0 1 222.8 70.9 L222.8 92.9 A100 46 0 0 0 223 90 Z" fill="var(--orange-side)"/>
          <path d="M222.8 70.9 A100 46 0 0 1 50.1 99.5 L50.1 121.5 A100 46 0 0 0 222.8 92.9 Z" fill="var(--grey-side)"/>
          <path d="M50.1 99.5 A100 46 0 0 1 23 68 L23 90 A100 46 0 0 0 50.1 121.5 Z" fill="var(--yellow-side)"/>
          <!-- top slices -->
          <path d="M123 68 L123 22 A100 46 0 0 1 181.8 30.8 Z" fill="var(--blue)"/>
          <path d="M123 68 L181.8 30.8 A100 46 0 0 1 222.8 70.9 Z" fill="var(--orange)"/>
          <path d="M123 68 L222.8 70.9 A100 46 0 0 1 50.1 99.5 Z" fill="var(--grey)"/>
          <path d="M123 68 L50.1 99.5 A100 46 0 0 1 64.2 30.8 Z" fill="var(--yellow)"/>
          <path d="M123 68 L64.2 30.8 A100 46 0 0 1 69.4 29.2 Z" fill="var(--olive)"/>
          <path d="M123 68 L69.4 29.2 A100 46 0 0 1 98.1 23.4 Z" fill="var(--green)"/>
          <path d="M123 68 L98.1 23.4 A100 46 0 0 1 123 22 Z" fill="#3a86c8"/>
        </g>
      </svg>
    </article>

    <article class="panel p-support">
      <h1 class="headline">Together We Can<span>Make a Difference</span></h1>
      <div class="rule"></div>
      <div class="support-box">
        <h2 class="tab">PATIENT SUPPORT</h2>
        <p>Mend ORX Syndrome, Inc. is a 501(c)(3) which was formed to drive efforts to cure diseases related to mutations of the Valosin Containing Protein(VCP) gene. Our main goal is to bring patients and doctors together so we can help one another and drive research towards a cure. We are also trying to bring awareness to the medical community about our rare disease.</p>
      </div>
      <p class="offer">We offer resources and support to patients,<br>caregivers and doctors. Connect with us.</p>
      <ul class="links">
        <li>IBMPFD Social page</li>
        <li>MendORX.org</li>
        <li>ORXinfo.org</li>
      </ul>
      <div class="contact">
        <svg width="14" height="18" viewBox="0 0 14 18"><path d="M7 1a5 5 0 0 0-5 5c0 4 5 9 5 9s5-5 5-9a5 5 0 0 0-5-5z" fill="none" stroke="var(--deep)" stroke-width="1.6"/><circle cx="7" cy="6" r="1.8" fill="var(--deep)"/><ellipse cx="7" cy="16.5" rx="5" ry="1.2" fill="none" stroke="var(--deep)"/></svg>
        Mend ORX Syndrome, Inc.<br>P.O. Box 4120 Linden, GA 30999
      </div>
      <div class="contact">
        <svg width="16" height="11" viewBox="0 0 16 11"><rect x="0.5" y="0.5" width="15" height="10" fill="var(--deep)"/><path d="M1 1l7 5 7-5" fill="none" stroke="#fff"/></svg>
        mendorxsyndrome@mailbox.org
      </div>
      <div class="contact">
        <svg width="14" height="14" viewBox="0 0 14 14"><g fill="none" stroke="var(--deep)" stroke-width="1.3"><circle cx="7" cy="7" r="6"/><ellipse cx="7" cy="7" rx="2.6" ry="6"/><path d="M1 7h12M2 4h10M2 10h10"/></g></svg>
        www.mendorx.org
      </div>
      <div class="badge" role="img" aria-label="Partner alliance membership badge"></div>
    </article>

    <article class="panel p-cover">
      <div class="brand"><i></i><b>Mend ORX Syndrome</b></div>
      <div class="ask"><div class="ask-in">
        <h2>Do you have a family history of ADULT ONSET</h2>
        <ul>
          <li><svg width="11" height="10" viewBox="0 0 11 10"><path d="M1 5l3 3 6-7" fill="none" stroke="#fff" stroke-width="1.8"/></svg>Muscle Weakness?</li>
          <li><svg width="11" height="10" viewBox="0 0 11 10"><path d="M1 5l3 3 6-7" fill="none" stroke="#fff" stroke-width="1.8"/></svg>Dementia?</li>
          <li><svg width="11" height="10" viewBox="0 0 11 10"><path d="M1 5l3 3 6-7" fill="none" stroke="#fff" stroke-width="1.8"/></svg>Bone Disease?</li>
          <li><svg width="11" height="10" viewBox="0 0 11 10"><path d="M1 5l3 3 6-7" fill="none" stroke="#fff" stroke-width="1.8"/></svg>ALS?</li>
          <li><svg width="11" height="10" viewBox="0 0 11 10"><path d="M1 5l3 3 6-7" fill="none" stroke="#fff" stroke-width="1.8"/></svg>Parkinson's?</li>
          <li><svg width="11" height="10" viewBox="0 0 11 10"><path d="M1 5l3 3 6-7" fill="none" stroke="#fff" stroke-width="1.8"/></svg>IBM?</li>
        </ul>
      </div></div>
      <div class="lab-photo" role="img" aria-label="Photo of a lab researcher with a pipette and microscope"></div>
      <div class="cover-band">You may consider talking to your doctor about a mutation of the VCP gene called</div>
      <div class="cover-name">IBMPFD</div>
      <div class="cover-foot">Inclusion Body Myopathy associated with Paget's Disease of Bone and Frontotemporal Dementia.<br><span class="pill">www.mendorx.org</span></div>
    </article>
  </section>

  <section class="spread spread--inside">
    <article class="panel p-symptoms">
      <h2 class="tab">SYMPTOMS:</h2>
      <div class="copy">
        <p class="just">IMBPFD, a VCP Disease, is an adult onset disorder that can affect the muscles, bones, and brain, and an affected patient may have any combination of the following conditions:</p>
        <h3 class="sub" style="margin-top:0">Inclusion Body Myopathy:</h3>
        <p class="just">The first symptom of IBMPFD is often muscle weakness (myopathy). Typically, patients first notice difficulty raising arms, losing balance or difficulty climbing stairs. As the disorder progresses, weakness develops in the other muscles in the arms, legs and core muscles. Muscle weakness can also affect respiratory and heart (cardiac) muscles. This disorder may first present in an individual's late 30's and over time occurs in approximately 90% of individuals with VCP Disease.</p>
        <h3 class="sub">Paget's disease of bone:</h3>
        <p class="just">Bone pain, particularly in the hips and spine, is usually the major symptom of Paget's disease. It most often affects bones of the hips, spine, and skull, and the long bones of the arms and legs. Paget's disease affects half of individuals with VCP Disease and typically first presents in a person's 30's or 40's, which is a much earlier age than those without VCP Disease.</p>
        <h3 class="sub">Frontotemporal Dementia:</h3>
        <p class="just">In about one-third of people with VCP Disease, the disorder also affects the brain. FTD typically changes personality, behavior, language and speech. FTD typically presents in the mid-50's.</p>
        <h3 class="sub">Amyotrophic Lateral Sclerosis (ALS or Lou Gehrig's disease):</h3>
        <p class="just">ALS occurs in approximately 10% of individuals with VCP Disease. Symptoms include increased muscle tone, weakness, muscle wasting, muscle</p>
      </div>
    </article>

    <article class="panel p-research">
      <div class="dna-photo" role="img" aria-label="Photo of a DNA helix inside a test tube held in a gloved hand"></div>
      <div class="rally"><b>Strength through numbers<br>will help</b><strong>US find a CURE!</strong></div>
      <h2 class="tab">RESEARCH:</h2>
      <div class="copy"><p class="just">The goal of the PRISM registry is to connect as many patients and researchers as possible to help advance treatments and cures for rare diseases.</p></div>
      <div class="enroll"><div>If you have been diagnosed with IBMPFD orVCPDisease, please help us by completing the patient registry through</div></div>
      <div class="site">Go to our website<b>WWW.MENDORX.ORG</b>to access the PRISM Registry.</div>
      <div class="copy low">
        <p class="just">The PRISM registry is free for patients to enroll and for researchers to access.</p>
        <p class="just">Please elect for researchers to have access to your registry, as that will greatly assist in the drive for a cure, especially when drug trials are recruiting patients.</p>
      </div>
      <div class="registry" role="img" aria-label="Registry footer with globe graphic"><b>PRISM Registry</b><small>Coordination of Rare Disease Research</small></div>
    </article>

    <article class="panel p-diag">
      <h2 class="tab">DIAGNOSIS:</h2>
      <div class="copy">
        <p class="just">The only way of diagnosing VCPDisease is through genetic testing. Consult with your doctor about testing for mutations of the VCP gene.</p>
        <p>For information about genetic testing, our two medical advisors are available as resources:</p>
        <div class="doc"><b>Dr. Helena Marsh,</b>Medical Geneticist at Westbrook University,<br><svg width="9" height="7" viewBox="0 0 9 7"><rect width="9" height="7" fill="var(--deep)"/><path d="M0 0l4.5 3.5L9 0" fill="none" stroke="#fff" stroke-width=".8"/></svg>hmarsh@westbrook.edu</div>
        <div class="doc"><b>Dr. Julian Ostrow,</b>Neuromuscular Specialist at Ridgeway University,<br><svg width="9" height="7" viewBox="0 0 9 7"><rect width="9" height="7" fill="var(--deep)"/><path d="M0 0l4.5 3.5L9 0" fill="none" stroke="#fff" stroke-width=".8"/></svg>jostrow@ridgeway.edu</div>
      </div>
      <div class="protein" role="img" aria-label="Ribbon diagram of the VCP protein structure with labelled domains"></div>
      <h2 class="tab treat">TREATMENTS:</h2>
      <div class="copy">
        <p class="just">There is an approved treatment for Paget's disease of bone, so early testing for this disorder is veryimportant.</p>
        <p class="just">There are no known cures or treatments for the Inclusion Body Myopathy or Frontotemporal Dementia. Consult with your doctor about physical therapy, stretching, diet and mobility</p>
      </div>
    </article>
  </section>

</main>
</body>
</html>
```